Informational Landing Page Redesign

Pure Stream Filter Guide, reviews and provides information about water ionizers for users. The web site is supposed to be an "expert or researched based" We are looking to redesign the following landing page:

http://www.purestreamfilterguide.example/learn/what-is-alkaline-water

The design should be geared towards converting visitors into leads. We are looking for a redesign of the content section. The header and footer should be the same as the current site. The text and colors should be consistent with the current site but please feel free to make bold choices that work and add stock photos.

Target Market(s)

Ages 45+ with disposable income.

Industry/Entity Type

Learn

Requirements
Must have
• The page must have the all current content. It also should have a web site form placed above the fold.

Please note you can change the designs of the "advertisements".
Nice to have
• Placement of social media elements so users can spread the page to friends, example facebook and google+ like buttons. A banner area that is capable of holding a rotating banner or video or banner.
Should not have
• Distractions from the goal, converting users to leads.
Distractions from the content, since the user is there to read.
Missing information and text, all information on the current page should appear on the redesign.

Deviations from the current header and footer.

```html
<!DOCTYPE html>
<html lang="en">
<head>
<meta charset="utf-8">
<title>Pure Stream Filter Guide – What is Alkaline Water?</title>
<link href="https://fonts.googleapis.com/css2?family=Open+Sans:wght@400;600;700&family=Arimo:wght@400;700&display=swap" rel="stylesheet">
<style>
:root{
  --page:#efefef;
  --ink:#222;
  --muted:#666;
  --logo:#6b6b6b;
  --nav:#1a7bc9;
  --link:#1f4fa3;
  --orange:#f68b1f;
  --orange-dark:#e07410;
  --panel:#eeedec;
  --panel-line:#d6d6d6;
  --start:#56655f;
  --hero-a:#1d55b7;
  --hero-b:#3f86d8;
  --deal:#1e7fc7;
  --yellow:#ffd320;
}
*{margin:0;padding:0;box-sizing:border-box}
html,body{width:946px;height:1200px;overflow:hidden}
body{background:linear-gradient(#ececec 0,#ffffff 110px,#f3f3f3 170px,var(--page) 400px);font-family:Arimo,Arial,sans-serif;color:var(--ink);position:relative}
a{text-decoration:none;color:var(--link)}
.abs{position:absolute}

/* brand */
.brand{display:flex;align-items:center;gap:10px}
.brand-dot{width:30px;height:30px;border-radius:50%;background:#2e8fe0;flex:none}
.brand-name{font-family:'Open Sans',sans-serif;font-weight:600;color:var(--logo);font-size:17px;line-height:19px;text-transform:uppercase}
.brand-tag{font-family:'Open Sans',sans-serif;font-size:9.5px;color:#7a7a7a;margin-top:3px}

/* nav */
.main-nav{left:408px;top:17px;width:388px;height:25px;border-top:1px solid #ddd;border-bottom:1px solid #ddd;display:flex;justify-content:space-around;align-items:center}
.main-nav a{font-family:'Open Sans',sans-serif;font-weight:700;font-size:12.5px;color:var(--nav)}
.btn-guide{left:717px;top:49px;width:79px;height:23px;background:var(--orange);border-radius:3px;color:#fff;font-family:'Open Sans',sans-serif;font-weight:700;font-size:9.5px;display:flex;align-items:center;justify-content:center}

/* hero */
.hero{left:141px;top:97px;width:665px;height:235px;border-radius:4px;overflow:hidden;background:linear-gradient(120deg,var(--hero-a),var(--hero-b))}
.hero-photo{position:absolute;right:0;top:0;width:300px;height:235px;background:radial-gradient(ellipse at 55% 60%,#e9f4fd 0,#9cc8ef 35%,rgba(63,134,216,0) 70%)}
.hero h1{position:absolute;left:34px;top:50px;font-family:'Open Sans',sans-serif;font-weight:400;font-size:16.5px;color:#fff}
.hero p{position:absolute;left:34px;top:80px;width:268px;font-size:8px;line-height:13.2px;color:#a9cdf5}
.hero-dots{position:absolute;left:34px;top:178px;display:flex;gap:2px}
.hero-dots span{width:10px;height:10px;border-radius:50%;background:#2f7ed3}
.hero-dots span:first-child{background:var(--orange)}

/* start here form */
.start{left:141px;top:349px;width:169px;height:189px;background:var(--start);border-radius:3px;border:1px solid #44524d}
.start h2{font-family:'Open Sans',sans-serif;font-weight:400;font-size:12px;color:#fff;padding:10px 10px 7px;border-bottom:1px solid #6e7d77}
.start p{font-size:7.5px;color:#fff;padding:7px 11px 6px}
.field{margin:0 11px 10px;height:20px;border-radius:5px;background:#f5f5f5;font-size:7.5px;color:#888;padding:5px 8px}
.btn-download{margin:2px 10px;width:79px;height:22px;border-radius:5px;background:linear-gradient(#ffa23b,var(--orange-dark));border:1px solid #c35f00;color:#5a2600;font-size:10px;display:flex;align-items:center;justify-content:center}

/* how it works */
.how{left:317px;top:349px;width:489px;height:189px;background:var(--panel);border:1px solid var(--panel-line);border-radius:3px}
.how h2{position:absolute;left:10px;top:10px;font-family:'Open Sans',sans-serif;font-weight:400;font-size:12px;color:#111}
.video{position:absolute;left:12px;top:36px;width:233px;height:131px;background:#111;padding:2px}
.video-still{width:229px;height:113px;background:linear-gradient(#2d5fa8,#5b8fd0 55%,#d7b9a2)}
.video-bar{height:14px;position:relative}
.video-bar i{position:absolute;left:0;top:2px;width:229px;height:2px;background:#555}
.video-bar b{position:absolute;left:0;top:2px;width:55px;height:2px;background:#d00}
.play{position:absolute;left:101px;top:48px;width:28px;height:18px}
.how p{position:absolute;left:250px;top:36px;width:230px;font-size:8px;line-height:16.6px;text-align:justify;color:#222}

/* article */
.article{left:141px;top:556px;width:462px}
.article h2{font-family:'Open Sans',sans-serif;font-weight:400;font-size:12px;margin-bottom:5px}
.article p{font-size:7.4px;line-height:12px;margin-bottom:12px;color:#222}
.minerals{display:flex;gap:18px;list-style:none;font-size:7.4px;margin:12px 0 26px 14px}
.minerals li::before,.learn li::before{content:"\00BB";font-weight:700;margin-right:6px}

/* pH scale graphic area */
.ph-graphic{left:628px;top:557px;width:166px;height:280px;background:linear-gradient(#f6c9c9,#f8e3b8 25%,#cfe8cf 45%,#c9d6f2 60%,#dccbf0 78%,#f4c6de);opacity:.85}

.divider{left:141px;top:855px;width:665px;height:1px;background:#cfcfcf}

/* bottom blocks */
.card{top:869px;height:199px;border:1px solid #d4d4d4;border-radius:4px;background:#fff;overflow:hidden}
.learn{left:141px;width:213px}
.learn h3{background:var(--orange);color:#fff;font-family:'Open Sans',sans-serif;font-weight:400;font-size:12px;height:36px;padding:10px 16px}
.learn ul{list-style:none;padding:11px 18px 0}
.learn li{font-size:7.5px;height:22.6px}
.learn a{display:block;font-size:7.5px;padding-left:18px;margin-top:-4px}
.club{left:366px;width:214px;background:linear-gradient(#f4f8ee,#dfeecd 60%,#cfe4b5)}
.deal{left:592px;width:214px;background:var(--deal);color:#fff;text-align:center;font-family:'Open Sans',sans-serif}
.deal .t1{font-size:14px;line-height:17px;margin-top:5px}
.deal .t1 b{font-weight:700}
.deal .t2{font-size:18px;font-weight:700;letter-spacing:2px;margin-top:6px}
.units{display:flex;justify-content:center;gap:22px;margin-top:6px}
.units div{width:46px;height:50px;border-radius:4px}
.units div:first-child{background:linear-gradient(#333,#111)}
.units div:last-child{background:linear-gradient(#eee,#aaa)}
.deal .t3{font-size:12px;margin-top:9px}
.deal .t4{font-size:18px;font-weight:700;color:var(--yellow);line-height:20px}
.deal .strip{position:absolute;left:0;bottom:0;width:100%;height:19px;background:#fff;color:var(--deal);font-size:12px;font-weight:700;line-height:19px}

/* footer */
.foot-line{left:141px;top:1097px;width:665px;height:1px;background:#dcdcdc}
.foot-copy{right:150px;top:1115px;font-family:'Open Sans',sans-serif;font-size:8.3px;color:#333}
.foot-nav{right:150px;top:1132px;display:flex;font-family:'Open Sans',sans-serif;font-size:9.5px}
.foot-nav a{color:var(--nav);padding:0 9px;border-left:1px solid #ccc}
.foot-nav a:first-child{border-left:0}
.foot-nav a:last-child{padding-right:0}
.social{right:150px;top:1151px;display:flex;gap:6px}
.social span{width:22px;height:22px;border-radius:4px;border:2px solid #333}
</style>
</head>
<body>

<header>
  <div class="abs" style="left:142px;top:17px">
    <div class="brand">
      <span class="brand-dot"></span>
      <div>
        <div class="brand-name">Pure Stream<br>Filter Guide</div>
        <div class="brand-tag">Find the perfect Water Ionizer.</div>
      </div>
    </div>
  </div>
  <nav class="abs main-nav">
    <a href="#">HOME</a><a href="#">REVIEWS</a><a href="#">LEARN</a><a href="#">COMPARE</a><a href="#">BLOG</a><a href="#">ABOUT US</a>
  </nav>
  <a class="abs btn-guide" href="#">Buyer's Guide</a>
</header>

<section class="abs hero">
  <div class="hero-photo" role="img" aria-label="Photo of water being poured into a glass with ice"></div>
  <h1>FILLED WITH HEALTHY MINERALS</h1>
  <p>Aenean sed lacus sapien, quis tempus est. Cras feugiat eleifend feugiat. Nam vestibulum, ligula viverra cursus fermentum, nisi est egestas lorem, sit amet elementum dolor purus in augue. Donec lacinia, elit id egestas scelerisque, velit sapien porta sapien, nec ornare purus nisi congue purus. Suspendisse ante est, congue eu vulputate sed, suscipit in ligula.</p>
  <div class="hero-dots"><span></span><span></span><span></span><span></span></div>
</section>

<form class="abs start">
  <h2>START HERE!</h2>
  <p>Download your free Buyer's Guide now!</p>
  <div class="field">Enter your name</div>
  <div class="field">Email</div>
  <div class="field">Phone</div>
  <div class="btn-download">DOWNLOAD</div>
</form>

<section class="abs how">
  <h2>HOW IT WORKS?</h2>
  <div class="video">
    <div class="video-still" role="img" aria-label="Video still of a woman drinking from a water bottle"></div>
    <svg class="play" viewBox="0 0 28 18"><rect width="28" height="18" rx="4" fill="#111"/><path d="M11 5l8 4-8 4z" fill="#fff"/></svg>
    <div class="video-bar"><i></i><b></b></div>
  </div>
  <p>Simply put, alkaline water is water with a potential hydrogen (pH) value of more than 7 (7 being neutral on the pH scale). Typically in the water ionizer industry, this is achieved using a process known as "electrodialysis". This process splits the neutral water into 2 types, acidic and alkaline. Both have their unique benefits and properties, but alkaline water is filled with healthy minerals like: Calcium, Magnesium, Potassium <a href="#">Read More...</a></p>
</section>

<article class="abs article">
  <h2>WHAT IS ALKALINE WATER?</h2>
  <p>The Water Ionizer industry is chalked full of confusing information. They often throw around machine specifications and technical jargon that needs to be dissected and explained in order to be understood. Our team at Pure Stream Filter Guide is hoping to avoid this by giving you only the facts you need. We have written this information coherently so you may understand the properties of alkaline water and how it benefits you. We want your next Water Ionizer purchase to be clear and informed. So let's start with the basics, what exactly is alkaline water?</p>
  <p>Simply put, alkaline water is water with a potential hydrogen (pH) value of more than 7 (7 being neutral on the pH scale). Typically in the water ionizer industry, this is achieved using a process known as "electrodialysis". This process splits the neutral water into 2 types, acidic and alkaline. Both have their unique benefits and properties, but alkaline water is filled with healthy minerals like:</p>
  <ul class="minerals"><li>Calcium</li><li>Magnesium</li><li>Potassium</li></ul>
  <p>While unhealthy minerals like fluoride, nitrates, and sulfides, are flushed out through the acidic water.</p>
  <p>Besides the ability to eliminate the harmful toxins that are found in most tap water, there are numerous health benefits to alkaline water – all of which are backed by research. Leaders in the health and fitness industry have attested to the advantages of alkaline water for years. Maybe it's time you discovered the real power of Alkaline Water for yourself?"</p>
  <p><a href="#">Continue Reading to Discover the Benefits of Alkaline Water</a></p>
</article>

<div class="abs ph-graphic" role="img" aria-label="Infographic of the pH scale from 0 to 14 with hydrogen ion concentrations and everyday example solutions"></div>

<div class="abs divider"></div>

<aside class="abs card learn">
  <h3>LEARN</h3>
  <ul>
    <li>What is Alkaline Water?</li>
    <li>Benefits of Alkaline Water</li>
    <li>What is Acidic Water?</li>
    <li>Benefits of Acidic Water</li>
    <li>What are pH and ORP?</li>
    <li>How do Ionizers work?</li>
  </ul>
  <a href="#">Read More...</a>
</aside>

<aside class="abs card club" role="img" aria-label="Advertisement for a wellness club with a leafy nutrition, fitness and mind and spirit illustration and a Join Today button"></aside>

<aside class="abs card deal">
  <div class="t1">Find the <b>best deals</b><br>on Water Ionizers</div>
  <div class="t2">GUARANTEED</div>
  <div class="units"><div role="img" aria-label="Black water ionizer unit"></div><div role="img" aria-label="Silver water ionizer unit"></div></div>
  <div class="t3">Talk to an expert today!</div>
  <div class="t4">(800) 555-0147</div>
  <div class="strip">IonizerDealDesk.example</div>
</aside>

<footer>
  <div class="abs foot-line"></div>
  <div class="abs" style="left:142px;top:1115px">
    <div class="brand">
      <span class="brand-dot"></span>
      <div>
        <div class="brand-name">Pure Stream<br>Filter Guide</div>
        <div class="brand-tag">Find the perfect Water Ionizer.</div>
      </div>
    </div>
  </div>
  <div class="abs foot-copy">© 2009-2012 Pure Stream Filter Guide. All Rights Reserved | Read our <a href="#" style="color:var(--nav)">Privacy Policy</a>.</div>
  <nav class="abs foot-nav">
    <a href="#">Home</a><a href="#">Reviews</a><a href="#">Learn</a><a href="#">Compare</a><a href="#">Blog</a><a href="#">About Us</a><a href="#">Buyer's Guide</a>
  </nav>
  <div class="abs social">
    <span style="background:#2f5fa8"></span><span style="background:#3a9a4a"></span><span style="background:#2aa7e0"></span><span style="background:#3f9a3a"></span>
  </div>
</footer>

</body>
</html>
```